Lantern Hill Publicity is a new boutique Press Office with a small roster of well-chosen clients across an array of disciplines; from Art and Technology to Restaurants and Fashion. Based in Greenpoint Brooklyn, Lantern Hill Publicity achieves outstanding results through hard work, tenacity, efficiency and a sense of humor. We need a simple, versatile and classic design. We would like each side of the card to be white text on a black background.

Boutique

```html
<!DOCTYPE html>
<html lang="en">
<head>
<meta charset="utf-8">
<title>Lantern Hill Publicity – Business Card</title>
<link href="https://fonts.googleapis.com/css2?family=Montserrat:wght@400;500&display=swap" rel="stylesheet">
<style>
  :root {
    --backdrop: #2a2a2a;
    --card: #0b0b0b;
    --ink: #ffffff;
    --ink-soft: #d9d9d9;
  }
  * { box-sizing: border-box; margin: 0; padding: 0; }
  html, body {
    width: 1200px;
    height: 900px;
    overflow: hidden;
    background: var(--backdrop);
    font-family: "Montserrat", sans-serif;
  }
  .canvas {
    position: relative;
    width: 1200px;
    height: 900px;
  }
  .card {
    position: absolute;
    width: 560px;
    height: 320px;
    background: var(--card);
    border-radius: 18px;
    color: var(--ink);
    box-shadow: 0 14px 30px rgba(0,0,0,0.45);
  }
  .card--front { left: 90px; top: 110px; }
  .card--back  { left: 550px; top: 470px; }

  /* Front: centered company name */
  .card--front .brand-name {
    position: absolute;
    inset: 0;
    display: flex;
    align-items: center;
    justify-content: center;
    text-align: center;
    font-weight: 500;
    font-size: 30px;
    letter-spacing: 0.14em;
    text-transform: uppercase;
    line-height: 1.35;
  }

  /* Back: name block left, contacts right */
  .card--back .brand-name {
    position: absolute;
    left: 44px;
    top: 0;
    bottom: 0;
    width: 250px;
    display: flex;
    align-items: center;
    font-weight: 500;
    font-size: 30px;
    letter-spacing: 0.06em;
    text-transform: uppercase;
    line-height: 1.2;
  }
  .contact {
    position: absolute;
    left: 330px;
    top: 52px;
    width: 215px;
    font-weight: 400;
  }
  .contact__name {
    font-size: 17px;
    letter-spacing: 0.04em;
    text-transform: uppercase;
  }
  .contact__title {
    font-size: 12px;
    color: var(--ink-soft);
    margin-top: 2px;
  }
  .contact__address {
    margin-top: 28px;
    font-size: 11.5px;
    line-height: 1.45;
    color: var(--ink-soft);
  }
  .contact__list {
    list-style: none;
    margin-top: 10px;
    font-size: 11.5px;
    color: var(--ink-soft);
  }
  .contact__list li {
    display: flex;
    align-items: center;
    gap: 10px;
    line-height: 1.9;
  }
  .contact__icon {
    width: 12px;
    height: 12px;
    flex: none;
  }
</style>
</head>
<body>
<main class="canvas">

  <section class="card card--front" aria-label="Card front">
    <h1 class="brand-name">Lantern Hill<br>Publicity</h1>
  </section>

  <section class="card card--back" aria-label="Card back">
    <p class="brand-name">Lantern Hill Publicity</p>

    <div class="contact">
      <p class="contact__name">Marcus T Avery</p>
      <p class="contact__title">President/CEO</p>

      <p class="contact__address">418 Calloway St #12<br>Brooklyn, NY 11222</p>

      <ul class="contact__list">
        <li>
          <svg class="contact__icon" viewBox="0 0 24 24" aria-hidden="true">
            <path fill="#fff" d="M6.6 10.8a15.1 15.1 0 0 0 6.6 6.6l2.2-2.2a1 1 0 0 1 1-.25 11.4 11.4 0 0 0 3.6.57 1 1 0 0 1 1 1V20a1 1 0 0 1-1 1A17 17 0 0 1 3 4a1 1 0 0 1 1-1h3.5a1 1 0 0 1 1 1c0 1.25.2 2.45.57 3.57a1 1 0 0 1-.25 1z"/>
          </svg>
          (718) 555-0142
        </li>
        <li>
          <svg class="contact__icon" viewBox="0 0 24 24" aria-hidden="true">
            <path fill="#fff" d="M2 11 22 2l-9 20-2.5-8.5z"/>
          </svg>
          info@lanternhillpr.com
        </li>
        <li>
          <svg class="contact__icon" viewBox="0 0 24 24" aria-hidden="true">
            <g fill="none" stroke="#fff" stroke-width="2">
              <circle cx="12" cy="12" r="9"/>
              <ellipse cx="12" cy="12" rx="4" ry="9"/>
              <path d="M3 12h18"/>
            </g>
          </svg>
          www.lanternhillpr.com
        </li>
      </ul>
    </div>
  </section>

</main>
</body>
</html>
```